Trade Show Booth

We need a Single booth design size and below are the requirements from the event holder.
How to provide graphics:
Single booth: Graphic size is 1993 mm width x 2483 mm height
Naming file: Name the files as Company name_ size_scale_bleed, for example: “Roam Kestal_1993x2483mm_scale1_10_ bleed50mm.”
Bleed & Marks: 50mm bleed all around, no marks, and no crop marks.
Resolution: Please try to keep graphics over 100 dpi to maintain good quality.

We are a DMC in Iceland and will be participating in a Travel show.
www.brightfjordtrips.example

We would like to work with someone who could help us create this and potentially some marketing material for the show.

```html
<!DOCTYPE html>
<html lang="en">
<head>
<meta charset="utf-8">
<title>Bright Fjord Trips – Booth Graphic</title>
<link rel="stylesheet" href="https://fonts.googleapis.com/css2?family=Poppins:wght@400;600;700;800&display=swap">
<style>
  :root {
    --navy: #252a78;
    --blue: #2e6db4;
    --sky: #b9e3f8;
    --ice: #eef5f7;
    --white: #ffffff;
    --glacier: #cfe0e8;
    --water: #3d4b58;
  }
  * { margin: 0; padding: 0; box-sizing: border-box; }
  html, body { width: 1002px; height: 1200px; overflow: hidden; }
  body { font-family: "Poppins", sans-serif; background: var(--sky); }
  .booth {
    position: relative; width: 1002px; height: 1200px; overflow: hidden;
    background: linear-gradient(180deg, var(--ice) 0%, var(--ice) 30%, var(--sky) 60%, var(--sky) 100%);
  }
  .lagoon-photo {
    position: absolute; left: 0; top: 360px; width: 1002px; height: 360px;
    background:
      linear-gradient(180deg, rgba(238,245,247,1) 0%, rgba(238,245,247,0) 18%),
      linear-gradient(180deg, #c9d9e1 0%, #dfe9ee 25%, #b7ccd8 48%, #5a6b78 62%, var(--water) 78%, rgba(185,227,248,1) 100%);
  }
  .brand-name {
    position: absolute; top: 150px; left: 0; width: 100%;
    text-align: center; font-weight: 800; font-size: 52px; letter-spacing: -1px;
    color: var(--navy);
  }
  .headline {
    position: absolute; top: 262px; left: 0; width: 100%;
    text-align: center; font-weight: 700; font-size: 52px; line-height: 60px;
    letter-spacing: -1.5px; color: var(--navy);
  }
  .web-pill {
    position: absolute; left: 254px; top: 389px; width: 500px; height: 48px;
    border-radius: 24px; background: var(--blue); color: var(--white);
    display: flex; align-items: center; justify-content: center;
    font-size: 22px; font-weight: 400;
    box-shadow: 0 6px 10px rgba(0,0,0,0.15);
  }
  .web-pill b { font-weight: 700; }
  .scene {
    position: absolute; border-radius: 50%; border: 15px solid var(--white);
    box-shadow: 0 10px 12px rgba(37,42,120,0.18);
  }
  .scene-falls { left: 81px; top: 620px; width: 246px; height: 246px;
    background: linear-gradient(160deg, #9aa7ad 0%, #e3e7e8 40%, #cfd6d8 65%, #4f8a3a 100%); }
  .scene-cliffs { left: 266px; top: 547px; width: 262px; height: 262px;
    background: linear-gradient(180deg, #6d9ad0 0%, #c7d8ea 30%, #2f4f78 48%, #4a3f35 65%, #7b6a58 100%); }
  .scene-columns { left: 674px; top: 547px; width: 246px; height: 246px;
    background: linear-gradient(100deg, #3f7ed0 0%, #8ab4e6 35%, #9b9c9b 55%, #c9c9c7 80%, #6f7070 100%); }
  .scene-gorge { left: 491px; top: 636px; width: 246px; height: 246px;
    background: linear-gradient(180deg, #9ec0e8 0%, #d3e2f0 25%, #3e6a2c 45%, #eef1f2 62%, #527a37 78%, #8a8a85 100%); }
  .tagline-bar {
    position: absolute; left: 180px; top: 919px; width: 518px; height: 62px;
    background: var(--blue); border-radius: 30px 0 0 30px;
    color: var(--white); font-size: 20px; line-height: 26px; text-align: center;
    display: flex; flex-direction: column; justify-content: center; padding-left: 50px;
  }
  .tagline-bar b { font-weight: 700; }
  .tap-icon {
    position: absolute; left: 143px; top: 920px; width: 58px; height: 58px;
    border-radius: 50%; background: var(--white); border: 2px solid var(--blue);
  }
  .email {
    position: absolute; left: 0; top: 996px; width: 1002px; padding-right: 110px;
    text-align: center; font-weight: 600; font-size: 22px; color: var(--navy);
    display: flex; align-items: center; justify-content: center; gap: 6px;
  }
  .badge-card {
    position: absolute; left: 697px; top: 918px; width: 170px; height: 170px;
    background: var(--white); border-radius: 6px;
  }
  .badge-mark {
    position: absolute; left: 16px; top: 14px; width: 138px; height: 142px;
    border-radius: 12px; background: linear-gradient(160deg, #3d5266, #9fb9c9 50%, #2e86b8);
  }
  .base-band { position: absolute; left: 0; bottom: 0; width: 100%; height: 16px; }
</style>
</head>
<body>
<main class="booth">
  <div class="lagoon-photo" role="img" aria-label="Photo of a glacier lagoon with floating icebergs under a pale sky"></div>

  <div class="brand-name">BRIGHT FJORD TRIPS</div>

  <h1 class="headline">LOCAL DMC &amp;<br>TRAVEL AGENCY IN ICELAND</h1>

  <div class="web-pill">www.<b>brightfjordtrips</b>.example</div>

  <div class="scene scene-falls" role="img" aria-label="Photo of a wide tiered waterfall in a grassy canyon"></div>
  <div class="scene scene-cliffs" role="img" aria-label="Photo of dark sea stacks on a rocky coastline"></div>
  <div class="scene scene-columns" role="img" aria-label="Photo of basalt column cliffs against a blue sky"></div>
  <div class="scene scene-gorge" role="img" aria-label="Photo of a tall waterfall between green cliffs"></div>

  <div class="tagline-bar">
    <span>Let us help you <b>plan and book your trip</b></span>
    <span>and make your planning <b>worry free.</b></span>
  </div>
  <div class="tap-icon">
    <svg width="54" height="54" viewBox="0 0 54 54" fill="none" stroke="#2e6db4" stroke-width="2.2" stroke-linecap="round" stroke-linejoin="round">
      <path d="M22 20 L22 38 L26 34 L29 41 L32 40 L29 33 L35 33 Z"/>
      <path d="M22 12 L22 15 M14 20 L17 20 M16 14 L18 16 M28 14 L26 16"/>
    </svg>
  </div>

  <div class="email">
    <svg width="22" height="22" viewBox="0 0 22 22">
      <circle cx="11" cy="11" r="10" fill="#2e6db4"/>
      <rect x="6" y="7.5" width="10" height="7" rx="1" fill="none" stroke="#fff" stroke-width="1.4"/>
      <path d="M6 8 L11 12 L16 8" fill="none" stroke="#fff" stroke-width="1.4"/>
    </svg>
    <span>contact@brightfjordtrips.example</span>
  </div>

  <div class="badge-card"><div class="badge-mark"></div></div>

  <svg class="base-band" viewBox="0 0 1002 16" preserveAspectRatio="none">
    <polygon points="0,0 515,0 501,16 0,16" fill="#2e6db4"/>
    <polygon points="507,16 521,0 1002,0 1002,16" fill="#252a78"/>
  </svg>
</main>
</body>
</html>
```